Customer Value Leaflet

We need a bi-fold brochure designing, based on the attached PDF wireframes. Our company name is mistralgrove.com (of which the logo is currently being designed). The corporate colour is orange (the exact shade of which we are happy to leave to the designers discretion).

The leaflet will distributed to customer experience experts and marketers so the design needs to be bright, engaging, clean and simple. Design is critical.

Industry/Entity Type

It Company

```html
<!DOCTYPE html>
<html lang="en">
<head>
<meta charset="utf-8">
<title>Customer Value Leaflet – mistralgrove.com</title>
<link rel="stylesheet" href="https://fonts.googleapis.com/css2?family=Source+Sans+3:wght@400;600;700&display=swap">
<style>
  :root {
    --orange: #f7941d;
    --black: #000000;
    --white: #ffffff;
    --band-grey: #c9c9cb;
    --arrow-grey: #a7a8ab;
    --arrow-grey-dark: #8e8f92;
    --ink: #111111;
  }
  * { margin: 0; padding: 0; box-sizing: border-box; }
  html, body { width: 1200px; height: 1200px; overflow: hidden; background: var(--white); }
  body { font-family: "Source Sans 3", "Myriad Pro", Arial, sans-serif; color: var(--ink); }
  .leaflet { position: relative; width: 1200px; height: 1200px; background: var(--white); }

  .headline-band {
    position: absolute; left: 0; top: 0; width: 1200px; height: 148px;
    background: var(--band-grey);
    display: flex; align-items: center; justify-content: center;
    font-size: 42px; color: var(--ink);
    padding-bottom: 8px;
  }

  .value-band {
    position: absolute; left: 0; top: 508px; width: 1200px; height: 342px;
    background: var(--orange);
  }
  .value-band__copy {
    position: absolute; top: 28px;
    color: var(--white); font-size: 42px; line-height: 56px; text-align: center;
    white-space: nowrap;
  }
  .value-band__copy--kim { left: 30px; width: 540px; }
  .value-band__copy--kevin { left: 650px; width: 545px; }

  .customer-card { position: absolute; top: 210px; height: 248px; display: flex; }
  .customer-card--kim { left: 54px; }
  .customer-card--kevin { left: 712px; }
  .customer-card__name {
    width: 124px; height: 100%; background: var(--black); color: var(--white);
    display: flex; align-items: center; justify-content: center;
  }
  .customer-card__name span {
    writing-mode: vertical-rl; transform: rotate(180deg);
    font-weight: 700; font-size: 38px;
  }
  .customer-card__value {
    height: 100%; background: var(--orange); color: var(--white);
    display: flex; flex-direction: column; align-items: center; justify-content: center;
    font-size: 84px; line-height: 92px; padding-bottom: 6px;
  }
  .customer-card--kim .customer-card__value { width: 322px; }
  .customer-card--kevin .customer-card__value { width: 319px; }

  .optimise-arrow { position: absolute; left: 500px; top: 148px; width: 200px; height: 806px; }
  .optimise-arrow__label {
    position: absolute; left: 557px; top: 200px; width: 84px; height: 620px;
    display: flex; align-items: flex-start; justify-content: center;
  }
  .optimise-arrow__label span {
    writing-mode: vertical-rl; font-size: 37px; letter-spacing: 1px; color: var(--ink);
    white-space: nowrap;
  }

  .closing-copy {
    position: absolute; left: 0; top: 980px; width: 1200px;
    text-align: center; font-size: 39px; line-height: 56px; color: var(--ink);
  }
  .closing-copy p { white-space: nowrap; }
  .closing-copy strong { font-weight: 700; }
</style>
</head>
<body>
<main class="leaflet">
  <header class="headline-band">Once you can calculate CLV…</header>

  <section class="value-band">
    <p class="value-band__copy value-band__copy--kim">you can personalise<br>Kim’s marketing<br>experience to grow her<br>lifetime value to be<br>more like Kevin’s</p>
    <p class="value-band__copy value-band__copy--kevin">you can understand<br>why Kevin is more<br>valuable and acquire<br>more customers<br>like him</p>
  </section>

  <svg class="optimise-arrow" viewBox="0 0 200 806" aria-hidden="true">
    <defs>
      <linearGradient id="arrowShade" x1="0" y1="0" x2="1" y2="0">
        <stop offset="0" stop-color="var(--arrow-grey-dark)"/>
        <stop offset="0.5" stop-color="var(--arrow-grey)"/>
        <stop offset="1" stop-color="var(--arrow-grey-dark)"/>
      </linearGradient>
    </defs>
    <polygon points="57,0 141,0 141,697 196,697 100,802 4,697 57,697" fill="url(#arrowShade)"/>
  </svg>
  <div class="optimise-arrow__label"><span>OPTIMISE YOUR MARKETING</span></div>

  <article class="customer-card customer-card--kim">
    <div class="customer-card__name"><span>Kim</span></div>
    <div class="customer-card__value"><span>CLV of</span><span>£149</span></div>
  </article>

  <article class="customer-card customer-card--kevin">
    <div class="customer-card__name"><span>Kevin</span></div>
    <div class="customer-card__value"><span>CLV of</span><span>£282</span></div>
  </article>

  <footer class="closing-copy">
    <p>We use data and science to predict how your customers</p>
    <p>will behave in future. Even if you already use CLV we</p>
    <p>can help you do and earn more… <strong>mistralgrove.com</strong></p>
  </footer>
</main>
</body>
</html>
```